BRASSWELL TARGET SPORTS, A modern indoor gun range comfortable for anyone to visit.

Please note the attached "Operating Plan", and "Letter of Introduction" for more details on our operation.

What we are looking for is the overall feel and look of the website. A lot of the details in how many links, what links, etc we will have built later. It's more important we get the right color scheme, flow, feel, etc.

This is an indoor gun range in Colorado. We are looking to be the fun lanes of the gun industry. We want a website that is simple, but stylish. Our range is forward thinking and modern. Please see our logo attached.

Our indoor range will also have a small cafe that will sell coffee, mixed soda drinks, and made from scratch cinnamon rolls.

Our look will be lighter colors. We want to avoid anything that would seem aggressive. Simple is the key here. We love simple clean designs. Pixel parlor has a good look and feel to it. Something with the same feel would be great. Our logo is red and black; however, we don't want the website to be dominated by those colors. Blue is also a great color.

We need a landing page that can shrink to different sizes of screens.
No mobile format.
Contact page with email submission
Menu will only have a couple links. We are open to different formats. Fun lanes format is also a good design.

Possible links will include: Home, Membership, About Us, Contact Us, Classes, Cafe

Target Market(s)

Primary target is male 35-55 years old with some college or more.

Number of Pages Required

3 page

Font styles to use
Sans Serif

Colors

Designer to choose colors to be used in the design.

Requirements
Must have
• Page 1 Landing first page
• Page 2 Blog posts to give updates on building progress
• Page 3 About us (hours of operation, etc)

```html
<!DOCTYPE html>
<html lang="en">
<head>
<meta charset="utf-8">
<title>Brasswell Target Sports</title>
<link href="https://fonts.googleapis.com/css2?family=Poppins:ital,wght@0,400;0,500;0,600;1,400&display=swap" rel="stylesheet">
<style>
  :root {
    --ink: #1b1b1b;
    --muted: #555a60;
    --accent: #d9361a;
    --paper: #ffffff;
    --rule: #e3e3e3;
    --band: #181b20;
    --hero-a: #3e3a33;
    --hero-b: #5a564c;
    --hero-c: #2b2925;
  }
  * { margin: 0; padding: 0; box-sizing: border-box; }
  html, body { width: 1200px; height: 622px; overflow: hidden; background: var(--paper); }
  body { font-family: "Poppins", sans-serif; color: var(--ink); position: relative; }

  .sidebar { position: absolute; left: 0; top: 0; width: 240px; height: 622px; background: var(--paper); }
  .brand { position: absolute; left: 38px; top: 44px; width: 170px; display: flex; align-items: center; gap: 8px; }
  .brand-dot { width: 14px; height: 14px; border-radius: 50%; background: var(--accent); flex: none; }
  .brand-name { font-weight: 600; font-size: 15px; line-height: 18px; color: var(--ink); letter-spacing: .3px; }
  .tagline { position: absolute; left: 0; width: 240px; top: 122px; text-align: center; font-style: italic; font-size: 12.5px; line-height: 21px; }

  .nav { position: absolute; left: 25px; top: 236px; list-style: none; }
  .nav li { font-size: 13.5px; height: 41.7px; letter-spacing: .1px; }

  .address { position: absolute; left: 25px; top: 454px; font-size: 14px; line-height: 21px; color: var(--muted); }
  .divider { position: absolute; left: 25px; top: 512px; width: 190px; height: 1px; background: var(--rule); }
  .tour-btn { position: absolute; left: 25px; top: 543px; width: 190px; height: 46px; background: var(--accent); color: #fff; font-size: 13.5px; display: flex; align-items: center; justify-content: center; }

  .hero { position: absolute; left: 240px; top: 0; width: 960px; height: 595px;
    background: radial-gradient(ellipse at 35% 45%, var(--hero-b) 0%, var(--hero-a) 45%, var(--hero-c) 100%); }
  .hero-photo { position: absolute; inset: 0; }
  .call { position: absolute; right: 218px; top: 60px; color: #fff; font-size: 14px; }
  .call b { font-weight: 600; }
  .headline { position: absolute; left: 73px; top: 343px; color: #fff; font-weight: 600; font-size: 44px; line-height: 64px; letter-spacing: -.3px; }
  .scroll-down { position: absolute; left: 461px; top: 514px; width: 37px; height: 37px; border-radius: 50%; background: #fff; display: flex; align-items: center; justify-content: center; }
  .band { position: absolute; left: 240px; top: 595px; width: 960px; height: 20px; background: var(--band); }
</style>
</head>
<body>
  <aside class="sidebar">
    <div class="brand">
      <span class="brand-dot"></span>
      <span class="brand-name">BRASSWELL TARGET SPORTS</span>
    </div>
    <p class="tagline">Colorado’s Finest Indoor<br>Shooting Range</p>
    <ul class="nav">
      <li>ABOUT US</li>
      <li>MEMBERSHIPS</li>
      <li>FAQS</li>
      <li>JOIN</li>
    </ul>
    <p class="address">Number, Street, City<br>State, Zip Code</p>
    <div class="divider"></div>
    <div class="tour-btn">Schedule a tour</div>
  </aside>

  <section class="hero">
    <div class="hero-photo" role="img" aria-label="Photo of a shooter wearing ear protection aiming a pistol down an indoor range lane"></div>
    <p class="call"><b>Call</b> 555-555-5555</p>
    <h1 class="headline">A Safe, Family Run, State of the<br>Art Indoor Shooting Range.</h1>
    <div class="scroll-down">
      <svg width="16" height="16" viewBox="0 0 16 16" fill="none" stroke="#1b1b1b" stroke-width="1.6" stroke-linecap="round" stroke-linejoin="round">
        <path d="M8 2v12M3 9l5 5 5-5"/>
      </svg>
    </div>
  </section>
  <div class="band"></div>
</body>
</html>
```